Business Card

Yes I would like you to design me a business card with the logo you just made me

Industry/Entity Type

Business

Colors
33b7a4
00a990
333333
000000
757575
7f7f7f

```html
<!DOCTYPE html>
<html lang="en">
<head>
<meta charset="utf-8">
<title>Mara Lenti Photography – Business Card</title>
<link rel="stylesheet" href="https://fonts.googleapis.com/css2?family=Open+Sans:wght@400&display=swap">
<style>
  :root {
    --page-bg: #ffffff;
    --card-light: #ece8e6;
    --pattern-tone-a: #e4dfdc;
    --pattern-tone-b: #d2cac7;
    --frame-dark: #333333;
    --card-dark: #3a3a3b;
    --brand-teal: #33b7a4;
    --text-light: #f2f2f2;
    --text-ink: #333333;
  }
  * { box-sizing: border-box; margin: 0; padding: 0; }
  html, body {
    width: 1200px;
    height: 900px;
    overflow: hidden;
    background: var(--page-bg);
    font-family: "Open Sans", Arial, sans-serif;
  }
  .canvas {
    position: relative;
    width: 1200px;
    height: 900px;
  }
  .card {
    position: absolute;
    top: 290px;
    width: 540px;
    height: 310px;
    border-radius: 26px;
    overflow: hidden;
    box-shadow: 0 14px 28px rgba(0,0,0,0.12);
  }
  /* Front */
  .card-front {
    left: 40px;
    background: var(--card-light);
    padding: 10px;
  }
  .card-front .frame {
    position: relative;
    width: 100%;
    height: 100%;
    border: 8px solid var(--frame-dark);
    border-radius: 20px;
    overflow: hidden;
  }
  .card-front .pattern-field {
    position: absolute;
    inset: 0;
    background: radial-gradient(ellipse at 50% 50%, var(--pattern-tone-a) 0%, var(--pattern-tone-b) 100%);
  }
  /* Back */
  .card-back {
    left: 620px;
    background: var(--card-dark);
  }
  /* Brand lockup */
  .brand {
    position: absolute;
    left: 0;
    right: 0;
    display: flex;
    flex-direction: column;
    align-items: center;
  }
  .brand-dot {
    border-radius: 50%;
  }
  .brand-name {
    font-weight: 400;
    text-align: center;
    line-height: 1.05;
  }
  .brand-name .tagline {
    display: block;
    letter-spacing: 0.32em;
    text-transform: uppercase;
  }
  .card-front .brand { top: 72px; }
  .card-front .brand-dot {
    width: 56px; height: 56px;
    background: var(--frame-dark);
    margin-bottom: 8px;
  }
  .card-front .brand-name { color: var(--text-ink); font-size: 42px; }
  .card-front .brand-name .tagline { font-size: 15px; margin-top: 4px; }

  .card-back .brand { top: 62px; }
  .card-back .brand-dot {
    width: 44px; height: 44px;
    background: var(--brand-teal);
    margin-bottom: 6px;
  }
  .card-back .brand-name { color: var(--brand-teal); font-size: 34px; }
  .card-back .brand-name .tagline { font-size: 12px; margin-top: 2px; }

  .contact-list {
    position: absolute;
    left: 32px;
    bottom: 50px;
    list-style: none;
    color: var(--text-light);
    font-size: 17px;
  }
  .contact-list li {
    display: flex;
    align-items: center;
    gap: 10px;
    line-height: 25px;
  }
  .contact-icon {
    width: 16px;
    height: 16px;
    flex: none;
  }
</style>
</head>
<body>
<main class="canvas">

  <section class="card card-front" aria-label="Business card front">
    <div class="frame">
      <div class="pattern-field" role="img" aria-label="Soft taupe floral damask pattern covering the card face"></div>
      <div class="brand">
        <span class="brand-dot"></span>
        <p class="brand-name">mara lenti<span class="tagline">photography</span></p>
      </div>
    </div>
  </section>

  <section class="card card-back" aria-label="Business card back">
    <div class="brand">
      <span class="brand-dot"></span>
      <p class="brand-name">mara lenti<span class="tagline">photography</span></p>
    </div>
    <ul class="contact-list">
      <li>
        <svg class="contact-icon" viewBox="0 0 16 16" aria-hidden="true">
          <rect x="3.5" y="1" width="9" height="14" rx="1.5" fill="var(--brand-teal)"/>
          <rect x="5" y="3" width="6" height="7" fill="var(--card-dark)"/>
          <circle cx="8" cy="12.5" r="1" fill="var(--card-dark)"/>
        </svg>
        555-014-2290
      </li>
      <li>
        <svg class="contact-icon" viewBox="0 0 16 16" aria-hidden="true">
          <rect x="1" y="3.5" width="14" height="10" rx="1" fill="var(--brand-teal)"/>
          <path d="M1.5 4.5 L8 9.5 L14.5 4.5" fill="none" stroke="var(--card-dark)" stroke-width="1.4"/>
        </svg>
        maralentiphoto@mailbox.com
      </li>
      <li>
        <svg class="contact-icon" viewBox="0 0 16 16" aria-hidden="true">
          <rect x="1.5" y="1.5" width="13" height="13" rx="2" fill="var(--brand-teal)"/>
        </svg>
        maralentiphotography
      </li>
    </ul>
  </section>

</main>
</body>
</html>
```